Private Villa in Bali looking for a flyer design

We need a flyer design for a 2bedrooms private villa with pool in Bali, called VILLA TESKA

Our villa is a private 2 bedrooms villa with private swimming pool, tranquil , luxurious, blending balinese and modern interiors , personal service and family home away from home
Out Motto : your blissful getaway

We would like an elegant, luxury and clean design

Colour scheme : BROWN, YELLOW/GOLD, GREY

It should have :
1/photo of the villa
2/ basic info of the villa
3/ location/address and location map of the villa

Villa Teska
Banjar Kelodsari,
Pererenan, Canggu
Bali - Indonesia

4/ website :
www.villateskamora

5/ email :
wulan@villateskamora.com

6/ Phone :
+852-47290516

I have attached some photos and the logo, please let me know if you need ai/eps file

Thank you . Please let me know if you need more information
Updates

-Trifold flyer on A4 size paper ( standard size flyer)

-Front page : Main photo and Logo
-Last page : Location map, email,website etc
-Page 2-4 : any design with photo and info from website 

Target Market(s)

Family, couples, honeymooners

Industry/Entity Type

It Service

Colors
ffc214
474747
9d9d9d

Requirements
Must have
• address, location map, website and email add, photos ( don't need to use all)

Trifold on A4 size paper double sided
Nice to have
• Trifold on A4 size paper
Should not have
• too many photos overlapping .

```html
<!DOCTYPE html>
<html lang="en">
<head>
<meta charset="utf-8">
<title>Villa Teska – Flyer</title>
<link href="https://fonts.googleapis.com/css2?family=Jost:wght@400;500&family=Sansita:ital,wght@1,700&display=swap" rel="stylesheet">
<style>
  :root {
    --page-bg: #a9a9a9;
    --paper: #ffffff;
    --charcoal-dark: #2f2f2f;
    --charcoal: #474747;
    --charcoal-light: #6a6a6a;
    --gold: #ffc214;
    --amber: #f5a623;
    --grey: #9d9d9d;
    --text-light: #f2f2f2;
  }
  * { box-sizing: border-box; margin: 0; padding: 0; }
  html, body { width: 1200px; height: 800px; overflow: hidden; }
  body {
    background: var(--page-bg);
    display: flex; align-items: center; justify-content: center;
    font-family: 'Jost', sans-serif;
  }
  .flyer {
    position: relative; width: 540px; height: 760px;
    background: radial-gradient(ellipse at 25% 48%, var(--charcoal-light) 0%, var(--charcoal) 40%, var(--charcoal-dark) 100%);
    overflow: hidden;
  }
  .hero-photo {
    position: absolute; left: 0; top: 0; width: 540px; height: 340px;
    background: linear-gradient(180deg, #eee9e2 0%, #d8cfc3 45%, #b25a3c 75%, #5c4a3e 100%);
    clip-path: path('M0 0 H540 V292 C450 267 360 272 270 300 C200 322 120 317 0 292 Z');
  }
  .brand-box {
    position: absolute; right: 26px; top: 28px; width: 98px; height: 84px;
    background: var(--paper);
    display: flex; flex-direction: column; align-items: center; justify-content: center; gap: 6px;
  }
  .brand-mark { width: 26px; height: 26px; background: var(--amber); }
  .brand-name { font-family: 'Jost', sans-serif; font-size: 14px; color: var(--charcoal); }
  .wave { position: absolute; left: 0; top: 0; width: 540px; height: 340px; pointer-events: none; }
  .badge {
    position: absolute; left: 202px; top: 250px; width: 124px; height: 124px; border-radius: 50%;
    background: var(--paper); padding: 5px;
  }
  .badge-ring { width: 100%; height: 100%; border-radius: 50%; background: var(--charcoal-dark); padding: 5px; }
  .badge-core {
    width: 100%; height: 100%; border-radius: 50%;
    background: radial-gradient(circle at 40% 35%, #ffd45a 0%, var(--amber) 75%);
    display: flex; align-items: center; justify-content: center; text-align: center;
    font-family: 'Sansita', sans-serif; font-style: italic; font-weight: 700;
    color: var(--paper); font-size: 23px; line-height: 1.05;
  }
  .info { position: absolute; left: 42px; top: 402px; width: 280px; }
  .info-title {
    font-family: 'Sansita', sans-serif; font-style: italic; font-weight: 700;
    color: var(--gold); font-size: 19px; margin-bottom: 10px;
  }
  .info-text { color: var(--text-light); font-size: 14px; line-height: 1.55; white-space: nowrap; }
  .gallery { position: absolute; left: 336px; top: 340px; width: 160px; display: flex; flex-direction: column; gap: 16px; }
  .gallery-photo { width: 160px; height: 104px; border: 2px solid #555; }
  .photo-pool { background: linear-gradient(180deg, #c9d3c8 0%, #4f6a45 50%, #3e8f8a 80%, #6b6b6b 100%); }
  .photo-bedroom { background: linear-gradient(135deg, #b8862e 0%, #e0a94a 45%, #6f4a22 100%); }
  .photo-lounge { background: linear-gradient(160deg, #7a3e1e 0%, #d48a3a 45%, #5a2a18 100%); }
  .map {
    position: absolute; left: 42px; top: 578px; width: 116px; height: 102px;
    background: linear-gradient(135deg, #e9ece9 0%, #dfe3e0 60%, #b7c9d8 100%);
  }
  .contact { position: absolute; left: 180px; top: 582px; width: 136px; color: var(--text-light); font-style: normal; }
  .contact-row { display: flex; align-items: flex-start; gap: 8px; font-size: 9px; line-height: 1.35; margin-bottom: 6px; }
  .contact-row.phone { font-size: 14px; font-weight: 500; align-items: center; margin-bottom: 8px; white-space: nowrap; }
  .contact-icon { width: 11px; height: 11px; flex: none; margin-top: 1px; }
  .phone .contact-icon { width: 12px; height: 16px; margin-top: 0; }
</style>
</head>
<body>
  <main class="flyer">
    <div class="hero-photo" role="img" aria-label="Photo of the villa's covered terrace lounge with red-cushioned rattan sofas"></div>
    <div class="brand-box">
      <span class="brand-mark"></span>
      <span class="brand-name">Villa Teska</span>
    </div>

    <svg class="wave" viewBox="0 0 540 340" aria-hidden="true">
      <path d="M0 292 C120 317 200 322 270 300 C360 272 450 267 540 292" fill="none" stroke="#ffffff" stroke-width="7"/>
    </svg>

    <div class="badge"><div class="badge-ring"><div class="badge-core">Villa<br>Teska</div></div></div>

    <section class="info">
      <h2 class="info-title">Basic info of the villa</h2>
      <p class="info-text">Our villa is a private 2 bedrooms<br>villa with private swimming pool,<br>tranquil , luxurious, blending balinese<br>and modern interiors , personal service<br>and family home away from home</p>
    </section>

    <div class="gallery">
      <div class="gallery-photo photo-pool" role="img" aria-label="Photo of the private pool and garden"></div>
      <div class="gallery-photo photo-bedroom" role="img" aria-label="Photo of a bedroom opening to the pool"></div>
      <div class="gallery-photo photo-lounge" role="img" aria-label="Photo of the living room with wooden ceiling"></div>
    </div>

    <div class="map" role="img" aria-label="Location map of the villa near the coast of Canggu"></div>

    <address class="contact">
      <div class="contact-row phone">
        <svg class="contact-icon" viewBox="0 0 12 16"><rect x="1" y="0.5" width="10" height="15" rx="2" fill="none" stroke="#ffc214" stroke-width="1.5"/><rect x="3" y="3" width="6" height="7" fill="#ffc214"/></svg>
        +852-47290516
      </div>
      <div class="contact-row">
        <svg class="contact-icon" viewBox="0 0 12 12"><circle cx="6" cy="6" r="5" fill="none" stroke="#ffc214" stroke-width="1.4"/><path d="M1 6h10M6 1c-3 3-3 7 0 10M6 1c3 3 3 7 0 10" fill="none" stroke="#ffc214" stroke-width="1"/></svg>
        www.villateskamora
      </div>
      <div class="contact-row">
        <svg class="contact-icon" viewBox="0 0 12 12"><rect x="0.5" y="2" width="11" height="8" fill="none" stroke="#ffc214" stroke-width="1.3"/><path d="M0.5 2l5.5 4.5L11.5 2" fill="none" stroke="#ffc214" stroke-width="1.3"/></svg>
        wulan@villateskamora.com
      </div>
      <div class="contact-row">
        <svg class="contact-icon" viewBox="0 0 12 12"><path d="M6 0.5L0.5 5.5H2V11.5H5V8H7V11.5H10V5.5H11.5Z" fill="#ffc214"/></svg>
        <span>Villa Teska<br>Banjar Kelodsari,<br>Pererenan, Canggu<br>Bali - Indonesia</span>
      </div>
    </address>
  </main>
</body>
</html>
```